Ardoise Lumen Stationery design

With my provided logo I need stationery design for business cards, envelope (#10), letterhead, fax sheet, memo sheet and 9'' x 12'' presentation folder. I would aIso need an email signature design included. PMS COLORS are : Pantone 541C et 299C. Looking for a bold look, minimalist yet eye-catching look.

```html
<!DOCTYPE html>
<html lang="en">
<head>
<meta charset="utf-8">
<title>Ardoise Lumen – Stationery</title>
<link href="https://fonts.googleapis.com/css2?family=Poppins:wght@300;400;500;600;800&family=Open+Sans:wght@400;700&display=swap" rel="stylesheet">
<style>
:root{
  --brand:#243a94;
  --brand-dark:#1f3387;
  --sky:#1fa3dd;
  --paper:#ffffff;
  --canvas:#e3e4e6;
  --ink:#4a4a4a;
  --faint:#f4f5f8;
  --line-on-blue:rgba(255,255,255,.35);
}
*{margin:0;padding:0;box-sizing:border-box}
html,body{width:1200px;height:1010px;overflow:hidden;background:var(--canvas)}
body{position:relative;font-family:'Poppins',sans-serif;color:var(--brand)}
.piece{position:absolute;overflow:hidden}
.sheet{background:var(--paper);width:333px;height:431px}
.blue{background:var(--brand);color:#fff}
.abs{position:absolute}

/* wordmark */
.mark{position:absolute;display:flex;align-items:center;gap:5px;font-weight:500;white-space:nowrap;line-height:1}
.mark i{display:block;border:1.5px solid currentColor}
.mark--sm{font-size:10px}.mark--sm i{width:11px;height:11px}
.mark--xs{font-size:7px;gap:4px}.mark--xs i{width:8px;height:8px;border-width:1px}
.mark--lg{font-size:23px;gap:10px}.mark--lg i{width:34px;height:34px;border-width:3px}
.mark--on-blue{color:#fff}

/* sheet header/footer */
.topbar{position:absolute;left:0;top:0;width:333px;height:12px}
.faint-band{position:absolute;background:var(--faint)}
.footer{position:absolute;left:0;bottom:0;width:333px;height:19px;border-top:1px solid var(--brand)}
.footer .ico{position:absolute;top:0;width:14px;height:19px;background:var(--brand);display:flex;align-items:center;justify-content:center}
.footer .txt{position:absolute;top:5px;font-size:6.3px;color:var(--brand);white-space:nowrap}
.ico svg{width:7px;height:7px;fill:#fff}

/* letterhead */
.headline{position:absolute;left:27px;top:86px;font-size:19px;font-weight:800;letter-spacing:.2px}
.headline-rule{position:absolute;left:27px;top:111px;width:63px;height:1.5px;background:var(--brand)}
.subtitle{position:absolute;left:27px;top:118px;font-family:'Open Sans',sans-serif;font-size:6.3px;color:var(--ink)}
.body-copy{position:absolute;left:27px;width:280px;font-family:'Open Sans',sans-serif;font-size:6.3px;line-height:12px;color:var(--ink);text-align:justify}
.closing{position:absolute;left:27px;font-family:'Open Sans',sans-serif;font-size:6.3px;color:var(--ink)}
.signature{position:absolute;left:27px;top:341px;width:52px;height:17px;background:linear-gradient(90deg,#e6e7ea,#f2f3f5);border-radius:2px}
.signer{position:absolute;left:27px;top:362px;font-family:'Open Sans',sans-serif;font-size:7.5px;font-weight:700;color:#555}
.signer-role{position:absolute;left:27px;top:373px;font-family:'Open Sans',sans-serif;font-size:6.3px;color:var(--ink)}

/* fax */
.fax-title{position:absolute;left:28px;top:96px;font-size:19px;font-weight:800}
.field{position:absolute;width:133px;height:11px;border-bottom:1px solid var(--brand);font-size:4.2px;font-weight:600;padding-left:6px;padding-top:4px}
.checks{position:absolute;left:29px;top:209px;width:275px;display:flex;justify-content:space-between;font-size:4.2px;font-weight:600}
.checks span{display:flex;align-items:center;gap:3px}
.checks span::before{content:"";width:5px;height:5px;border:.8px solid var(--brand)}
.checks-rule{position:absolute;left:29px;top:225px;width:275px;height:1px;background:var(--brand)}
.note{position:absolute;left:39px;top:237px;font-size:4.2px;font-weight:600}

/* lines on blue */
.vl{position:absolute;width:1px;background:var(--line-on-blue)}
.hl{position:absolute;height:1px;background:var(--line-on-blue)}
.shade{position:absolute;background:var(--brand-dark)}

/* envelope */
.window{position:absolute;left:171px;top:41px;width:155px;height:74px;background:#fff;border-radius:8px}
.contact-row{position:absolute;display:flex;gap:9px;font-size:4px;color:#fff;white-space:nowrap}
.contact-row span{display:flex;align-items:center;gap:3px}
.contact-row svg{width:4.5px;height:4.5px;fill:#fff}

/* email signature */
.frame{position:absolute;border:.8px solid var(--line-on-blue)}
.portrait{position:absolute;left:28px;top:17px;width:39px;height:48px;background:linear-gradient(160deg,#6f9bc4,#3d5f86)}
.sig-name{position:absolute;left:97px;top:15px;font-size:8px;font-weight:400}
.sig-name b{font-weight:600}
.sig-role{position:absolute;left:97px;top:26px;font-size:4.2px;font-weight:500}
.stack{position:absolute;display:flex;flex-direction:column;gap:5px;font-size:4.2px;color:#fff;white-space:nowrap}
.stack span{display:flex;align-items:center;gap:4px}
.stack svg{width:4.5px;height:4.5px;fill:#fff}
.sig-divider{position:absolute;left:167px;top:17px;width:.8px;height:50px;background:var(--line-on-blue)}
.sig-blurb{position:absolute;left:180px;top:16px;width:66px;font-size:3.5px;line-height:4.3px;font-weight:500;color:#fff}

/* folder back */
.contact-big{position:absolute;left:0;height:24px;display:flex;align-items:center}
.contact-big .ico{width:27px;height:24px;background:var(--brand);display:flex;align-items:center;justify-content:center}
.contact-big .ico svg{width:11px;height:11px;fill:#fff}
.contact-big .txt{margin-left:7px;font-size:13.5px;font-weight:300;color:#444;white-space:nowrap}
</style>
</head>
<body>

<svg width="0" height="0" style="position:absolute">
  <defs>
    <symbol id="i-phone" viewBox="0 0 10 10"><path d="M3 0h4a1 1 0 0 1 1 1v8a1 1 0 0 1-1 1H3a1 1 0 0 1-1-1V1a1 1 0 0 1 1-1zm0 1.3v6.6h4V1.3z"/></symbol>
    <symbol id="i-mail" viewBox="0 0 10 10"><path d="M0 2h10v6H0zm1 .8 4 2.7 4-2.7z"/></symbol>
    <symbol id="i-pin" viewBox="0 0 10 10"><path d="M5 0a3.5 3.5 0 0 1 3.5 3.5C8.5 6 5 10 5 10S1.5 6 1.5 3.5A3.5 3.5 0 0 1 5 0zm0 2.2a1.3 1.3 0 1 0 0 2.6 1.3 1.3 0 0 0 0-2.6z"/></symbol>
  </defs>
</svg>

<!-- Letterhead -->
<section class="piece sheet letterhead" style="left:66px;top:57px">
  <div class="faint-band" style="left:226px;top:12px;width:10px;height:140px"></div>
  <div class="faint-band" style="left:226px;top:142px;width:107px;height:10px"></div>
  <div class="faint-band" style="left:98px;top:320px;width:10px;height:92px"></div>
  <svg class="topbar" viewBox="0 0 333 12"><path d="M0 0h333v7H110l-7-3H0z" fill="var(--brand)"/><rect x="104" y="10" width="229" height="1.2" fill="var(--brand)"/></svg>
  <div class="mark mark--sm" style="left:27px;top:40px;color:var(--brand)"><i></i>Ardoise Lumen</div>
  <h1 class="headline">HEADLINE</h1>
  <div class="headline-rule"></div>
  <p class="subtitle">Lorem Ipsum Dolor Sit Amet</p>
  <p class="body-copy" style="top:141px">Consectetur adipiscing elit. Duis eu semper turpis, non pulvinar mauris. Aenean et eros in justo pretium laoreet. Pellentesque pharetra purus dui, non vestibulum arcu dapibus at. Lorem ipsum dolor sit amet, consectetur adipiscing elit. Curabitur neque mauris, lobortis sed sem nec, iaculis hendrerit tellus. Pellentesque purus odio, ullamcorper non scelerisque nec, auctor et dui. In hac habitasse platea dictumst. Maecenas convallis ante sapien. In lacinia volutpat commodo. Mauris congue arcu non dui pretium volutpat. Quisque augue urna, pretium sed metus eget, mollis consectetur nunc. Donec laoreet turpis nec mi ultrices, at vulputate felis vestibulum.</p>
  <p class="body-copy" style="top:248px">Integer blandit ut eros quis dictum. Pellentesque vel enim commodo, accumsan purus id, scelerisque metus. Donec volutpat lacinia enim in aliquet. Fusce t sagittis ultrices. Pellentesque ac est ornare, lobortis erat aliquet, malesuada turpis. Praesent non massa nec purus posuere vehicula ac ac felis. Nunc eleifend euismod orci. Phasellus quis faucibus erat.</p>
  <p class="closing" style="top:324px">Sincerely,</p>
  <div class="signature" role="img" aria-label="Handwritten signature"></div>
  <p class="signer">Lucien R. Vautrin</p>
  <p class="signer-role">Company Director</p>
  <footer class="footer">
    <span class="ico" style="left:27px"><svg><use href="#i-phone"/></svg></span><span class="txt" style="left:47px">+1 48 715 290 4</span>
    <span class="ico" style="left:120px"><svg><use href="#i-mail"/></svg></span><span class="txt" style="left:143px">hi@ardoiselumen.com</span>
    <span class="ico" style="left:225px"><svg><use href="#i-pin"/></svg></span><span class="txt" style="left:249px">Rue Verte house #14</span>
  </footer>
</section>

<!-- Envelope #10 -->
<section class="piece blue envelope" style="left:430px;top:57px;width:352px;height:157px">
  <div class="shade" style="left:20px;top:0;width:12px;height:157px;opacity:.5"></div>
  <div class="vl" style="left:135px;top:0;height:54px"></div>
  <div class="hl" style="left:108px;top:54px;width:63px"></div>
  <div class="hl" style="left:0;top:103px;width:135px"></div>
  <div class="vl" style="left:108px;top:103px;height:54px"></div>
  <div class="mark mark--sm mark--on-blue" style="left:51px;top:75px"><i></i>Ardoise Lumen</div>
  <div class="window"></div>
  <div class="contact-row" style="left:170px;top:134px">
    <span><svg><use href="#i-phone"/></svg>+1 48 715 290 4</span>
    <span><svg><use href="#i-mail"/></svg>hi@ardoiselumen.com</span>
    <span><svg><use href="#i-pin"/></svg>Rue Verte house #14</span>
  </div>
</section>

<!-- Email signature -->
<section class="piece blue email-signature" style="left:430px;top:263px;width:359px;height:82px">
  <div class="frame" style="left:15px;top:6px;width:52px;height:59px"></div>
  <div class="frame" style="left:28px;top:17px;width:51px;height:59px"></div>
  <div class="portrait" role="img" aria-label="Portrait photo of the team member"></div>
  <p class="sig-name"><b>MARC</b> Delorme</p>
  <p class="sig-role">PRODUCT MANAGER</p>
  <div class="stack" style="left:97px;top:43px">
    <span><svg><use href="#i-phone"/></svg>+1 48 715 290 4</span>
    <span><svg><use href="#i-mail"/></svg>hi@ardoiselumen.com</span>
    <span><svg><use href="#i-pin"/></svg>Rue Verte house #14</span>
  </div>
  <div class="sig-divider"></div>
  <p class="sig-blurb">Consectetur adipiscing elit. Duis eu semper turpis, non pulvinar mauris. Aenean et eros in justo pretium laoreet. Pellentesque pharetra purus dui, non vestibulum arcu dapibus at. Lorem ipsum dolor sit amet, curabitur neque mauris, lobortis sed sem nec, iaculis hendrerit tellus ullamcorper nunc.</p>
  <div class="mark mark--sm mark--on-blue" style="left:263px;top:36px"><i></i>Ardoise Lumen</div>
</section>

<!-- Business card front -->
<section class="piece blue card-front" style="left:431px;top:403px;width:137px;height:78px">
  <div class="vl" style="left:76px;top:0;height:26px"></div>
  <div class="hl" style="left:76px;top:26px;width:61px"></div>
  <div class="hl" style="left:0;top:54px;width:61px"></div>
  <div class="vl" style="left:61px;top:54px;height:24px"></div>
  <div class="mark mark--xs mark--on-blue" style="left:38px;top:36px"><i></i>Ardoise Lumen</div>
</section>

<!-- Business card back -->
<section class="piece blue card-back" style="left:583px;top:403px;width:137px;height:78px">
  <div class="mark mark--xs mark--on-blue" style="left:14px;top:36px;font-size:5.5px"><i></i>Ardoise Lumen</div>
  <div class="sig-divider" style="left:68px;top:27px;height:24px"></div>
  <div class="stack" style="left:78px;top:28px;font-size:3.8px;gap:4px">
    <span><svg><use href="#i-phone"/></svg>+1 48 715 290 4</span>
    <span><svg><use href="#i-mail"/></svg>hi@ardoiselumen.com</span>
    <span><svg><use href="#i-pin"/></svg>Rue Verte house #14</span>
  </div>
</section>

<!-- Fax sheet -->
<section class="piece sheet fax" style="left:66px;top:538px">
  <div class="faint-band" style="left:226px;top:12px;width:10px;height:140px"></div>
  <div class="faint-band" style="left:226px;top:142px;width:107px;height:10px"></div>
  <div class="faint-band" style="left:98px;top:320px;width:10px;height:92px"></div>
  <svg class="topbar" viewBox="0 0 333 12"><path d="M0 0h333v7H110l-7-3H0z" fill="var(--brand)"/><rect x="104" y="10" width="229" height="1.2" fill="var(--brand)"/></svg>
  <div class="mark mark--sm" style="left:27px;top:40px;color:var(--brand)"><i></i>Ardoise Lumen</div>
  <h1 class="fax-title">Fax</h1>
  <div class="field" style="left:29px;top:129px">To:</div>
  <div class="field" style="left:171px;top:129px">From:</div>
  <div class="field" style="left:29px;top:147px">Fax:</div>
  <div class="field" style="left:171px;top:147px">Pages:</div>
  <div class="field" style="left:29px;top:165px">Phone:</div>
  <div class="field" style="left:171px;top:165px">Date:</div>
  <div class="field" style="left:29px;top:182px">Re:</div>
  <div class="field" style="left:171px;top:182px">CC:</div>
  <div class="checks"><span>Urgent</span><span>For Review</span><span>Please Comment</span><span>Please Reply</span><span>Please Recycle</span></div>
  <div class="checks-rule"></div>
  <p class="note">Note</p>
  <footer class="footer">
    <span class="ico" style="left:27px"><svg><use href="#i-phone"/></svg></span><span class="txt" style="left:47px">+1 48 715 290 4</span>
    <span class="ico" style="left:120px"><svg><use href="#i-mail"/></svg></span><span class="txt" style="left:143px">hi@ardoiselumen.com</span>
    <span class="ico" style="left:225px"><svg><use href="#i-pin"/></svg></span><span class="txt" style="left:249px">Rue Verte house #14</span>
  </footer>
</section>

<!-- Presentation folder, front -->
<section class="piece blue folder-front" style="left:431px;top:538px;width:332px;height:431px">
  <div class="shade" style="left:114px;top:0;width:10px;height:130px;opacity:.6"></div>
  <div class="shade" style="left:210px;top:300px;width:10px;height:131px;opacity:.6"></div>
  <div class="vl" style="left:172px;top:0;height:189px"></div>
  <div class="hl" style="left:172px;top:189px;width:160px"></div>
  <div class="hl" style="left:0;top:250px;width:186px"></div>
  <div class="vl" style="left:160px;top:250px;height:181px"></div>
  <div class="mark mark--lg mark--on-blue" style="left:92px;top:197px"><i></i>Ardoise Lumen</div>
</section>

<!-- Presentation folder, back -->
<section class="piece sheet folder-back" style="left:795px;top:538px">
  <div class="faint-band" style="left:115px;top:0;width:10px;height:172px"></div>
  <div class="faint-band" style="left:0;top:162px;width:125px;height:10px"></div>
  <div class="faint-band" style="left:180px;top:269px;width:10px;height:162px"></div>
  <div class="faint-band" style="left:180px;top:269px;width:153px;height:10px"></div>
  <div class="mark mark--lg" style="left:93px;top:197px;color:var(--brand)"><i></i>Ardoise Lumen</div>
  <div class="abs" style="left:27px;top:317px;width:1px;height:114px;background:var(--brand)"></div>
  <div class="contact-big" style="top:317px"><span class="ico"><svg><use href="#i-phone"/></svg></span><span class="txt">+1 48 715 290 4</span></div>
  <div class="contact-big" style="top:352px"><span class="ico"><svg><use href="#i-mail"/></svg></span><span class="txt">hi@ardoiselumen.com</span></div>
  <div class="contact-big" style="top:387px"><span class="ico"><svg><use href="#i-pin"/></svg></span><span class="txt">Rue Verte house #14</span></div>
</section>

</body>
</html>
```